Lanternway Circle Monthly Giving Flyer

We need a flyer to promote a monthly giving program called Lanternway Circle to support our nonprofit organization, Brightpath Youth Trust. We have a group of students from Uganda travelling across the country in a performing arts group called Voices of Korali. While they are on tour we want audience members to sign up to become monthly donors and support our ongoing educational work in Uganda. This flyer will be on the info table, in seats, and handed out throughout the course of the tour.

Lanternway Circle is a new program. The idea is that the audience members will be motivated by their interaction with the students to fill in their information to sign up to make a monthly gift. In exchange, we'll give them a free merchandise item (CD, tshirt, etc) for signing up and we'll send them special updates from the students throughout the year electronically.

Check out BrightpathYouthTrust.org for more info about our programs, Lanternway Circle and our branding/style.

This will be printed as a 5x7 two-sided postcard that we can print cheaply in color.

Side 1: Draw attention to the program graphically with a message of "Join Us Become an Lanternway Member," happy student image, etc. You can download an image from the gallery on our website, if you choose at: http://www.brightpathyouthtrust.org/who-we-are/media/ (scroll to the bottom)

Side 2: Lead in text: Join our network of friends committed to supporting the ongoing education of Brightpath scholars through monthly donations. As an Lanternway Member, you play a critical role by helping ensure that we can provide the life-changing services to our scholars month in and month out.
We'll send you special updates from the students throughout the year to keep you up to date on how your gifts are impacting lives.

I'd like to give $25, $50, $75, $100, or $____ other amount
Name, address, phone number, email
Credit card #, expiration, and security code
I've provided a voided check for monthly electronic funds transfer

Requirements
Nice to have
• We have not created a logo or done any branding for Lanternway Circle so it would be nice to have a nicely designed logo/font for Lanternway Circle incorporated into the flyer design that we can in other places as well to promote the program.
Should not have
• Anything that play on the poverty or challenges in Africa. We try to provide always positive image of Africa and the students we work with.

```html
<!DOCTYPE html>
<html lang="en">
<head>
<meta charset="utf-8">
<title>Lanternway Circle Monthly Giving Postcard</title>
<link rel="stylesheet" href="https://fonts.googleapis.com/css2?family=Source+Sans+3:wght@400;600;700&display=swap">
<style>
  :root {
    --orange: #f39322;
    --orange-light: #f7b152;
    --brown: #5b3a1f;
    --ink: #2b2b2b;
    --paper: #ffffff;
    --backdrop: #e9e6e2;
    --photo-dark: #6e6a66;
    --photo-mid: #a9a5a1;
    --photo-light: #dcdad8;
  }
  * { box-sizing: border-box; margin: 0; padding: 0; }
  html, body { width: 962px; height: 1200px; overflow: hidden; }
  body {
    background: var(--backdrop);
    font-family: "Source Sans 3", Arial, sans-serif;
    color: var(--ink);
    position: relative;
  }
  .card {
    position: absolute;
    left: 101px;
    width: 760px;
    height: 540px;
    background: var(--paper);
    overflow: hidden;
    box-shadow: 0 3px 10px rgba(0,0,0,.18);
  }
  .card--front { top: 40px; }
  .card--back { top: 620px; }

  .top-strip {
    position: absolute; left: 0; top: 0; width: 100%; height: 12px;
    background: var(--orange);
  }

  .brand {
    position: absolute;
    display: flex; align-items: center; gap: 10px;
  }
  .brand__dot {
    width: 66px; height: 66px; border-radius: 50%;
    background: var(--orange);
    flex: none;
  }
  .brand__name {
    font-weight: 600;
    color: var(--brown);
    font-size: 21px;
    line-height: 1.05;
    letter-spacing: .3px;
  }

  /* front */
  .card--front .brand { left: 34px; top: 62px; }
  .headline {
    position: absolute; left: 292px; top: 50px;
    color: var(--brown);
    font-weight: 400;
    font-size: 39px;
    line-height: 1.15;
  }
  .headline strong { font-weight: 700; display: block; }
  .front-photo {
    position: absolute; left: 0; top: 168px; width: 100%; height: 372px;
    background: linear-gradient(180deg, var(--photo-light) 0%, var(--photo-mid) 35%, #5a4a44 100%);
  }
  .url-band {
    position: absolute; left: 0; width: 100%;
    background: var(--orange);
    display: flex; align-items: center;
  }
  .card--front .url-band {
    top: 462px; height: 38px;
    justify-content: flex-end; padding-right: 120px;
    color: var(--paper); font-size: 22px; font-weight: 600;
  }

  /* back */
  .back-copy {
    position: absolute; left: 38px; top: 32px; width: 360px;
    font-size: 12.5px; line-height: 15px;
  }
  .lead {
    color: var(--orange); font-weight: 700; margin-bottom: 14px;
  }
  .back-copy p + p { margin-top: 12px; }
  .divider {
    position: absolute; left: 38px; top: 222px; width: 345px; height: 1px;
    background: #cfcfcf;
  }
  .gift-bar {
    position: absolute; left: 26px; top: 236px; width: 340px; height: 24px;
    background: var(--brown);
    color: var(--paper); font-weight: 700; font-size: 14.5px;
    padding: 2px 0 0 14px;
    clip-path: polygon(2% 0, 100% 10%, 97% 100%, 0 90%);
  }
  .amounts {
    position: absolute; left: 38px; top: 270px;
    font-size: 13px; display: flex; gap: 5px; align-items: center;
  }
  .box {
    display: inline-block; width: 10px; height: 10px;
    border: 1.5px solid var(--orange); background: #fde3bf;
    margin-right: 2px; vertical-align: -1px;
  }
  .form {
    position: absolute; left: 38px; top: 294px; width: 345px;
    font-size: 13px; line-height: 16px;
  }
  .row { display: flex; gap: 4px; align-items: flex-end; }
  .field { display: inline-block; border-bottom: 1px solid var(--ink); height: 12px; }
  .grow { flex: 1; }
  .note { margin-top: 14px; }

  .back-side {
    position: absolute; left: 400px; top: 0; width: 360px; height: 500px;
    background: #f3f3f3;
  }
  .back-photo {
    position: absolute; left: 400px; top: 150px; width: 360px; height: 350px;
    background: linear-gradient(180deg, #efefef 0%, var(--photo-light) 30%, var(--photo-mid) 100%);
  }
  .card--back .brand { left: 428px; top: 48px; }
  .card--back .url-band {
    top: 500px; height: 40px; justify-content: center;
    color: var(--brown); font-size: 17px; font-weight: 600;
  }
</style>
</head>
<body>

<section class="card card--front">
  <div class="top-strip"></div>
  <div class="brand">
    <span class="brand__dot"></span>
    <span class="brand__name">Brightpath<br>Youth Trust</span>
  </div>
  <h1 class="headline">Join Us! Become an <strong>Lanternway Member</strong></h1>
  <div class="front-photo" role="img" aria-label="Photo of four smiling students in school uniforms standing together outdoors"></div>
  <div class="url-band">www.BrightpathYouthTrust.org</div>
</section>

<section class="card card--back">
  <div class="top-strip"></div>
  <div class="back-side"></div>
  <div class="back-photo" role="img" aria-label="Faded photo of a student performer in costume"></div>
  <div class="brand">
    <span class="brand__dot"></span>
    <span class="brand__name">Brightpath<br>Youth Trust</span>
  </div>

  <div class="back-copy">
    <p class="lead">Read Join our network of friends Support the ongoing education of Brightpath scholars through monthly donations.</p>
    <p>As an Lanternway Member, you play a critical role by helping ensure that we can provide the life-changing services to our scholars month in and month out.</p>
    <p>We'll send you special updates from the students throughout the year to keep you up to date on how your gifts are impacting lives.</p>
  </div>
  <div class="divider"></div>
  <div class="gift-bar">read I'd like to give a monthly gift of:</div>
  <div class="amounts">
    <span><span class="box"></span>$25,</span>
    <span><span class="box"></span>$50,</span>
    <span><span class="box"></span>$75,</span>
    <span><span class="box"></span>$100, or</span>
    <span><span class="box"></span>$___other amount</span>
  </div>
  <div class="form">
    <div class="row">Name :<span class="field grow"></span></div>
    <div class="row">Address :<span class="field grow"></span></div>
    <div class="row">City :<span class="field" style="width:95px"></span>State :<span class="field" style="width:32px"></span>Zip :<span class="field grow"></span></div>
    <div class="row">Phone Number :<span class="field grow"></span></div>
    <div class="row">Email :<span class="field" style="width:150px"></span></div>
    <div class="row">Credit Card :<span class="field grow"></span></div>
    <div class="row">Expiration<span class="field" style="width:36px"></span>Security Code<span class="field" style="width:100px"></span></div>
    <p class="note">I've provided a voided check for monthly<br>electronic funds transfer</p>
  </div>

  <div class="url-band">www.BrightpathYouthTrust.org</div>
</section>

</body>
</html>
```